Business card design needed

My company specialises in carpentry and building services.
Based in Brisbane QLD
We also do:
property maintenance
plastering
painting
tiling
property maintenance

Industry/Entity Type

Carpentry

Contact Information for Business Card

RT Services QLD
Mark 0412583047
Dean 0493217586

```html
<!DOCTYPE html>
<html lang="en">
<head>
<meta charset="utf-8">
<title>RT Services QLD – Business Card</title>
<link rel="stylesheet" href="https://fonts.googleapis.com/css2?family=Arimo:wght@400;500&display=swap">
<style>
  :root {
    --page-bg: #e9e7e4;
    --card-light: #f4f4f4;
    --card-mid: #cfcfcf;
    --card-edge: #a9a9a9;
    --band: #2f2f2f;
    --ink-dark: #3e3e3e;
    --ink-mid: #5c5c5c;
    --ink-light: #f2f2f2;
    --ink-soft: #d8d8d8;
    --divider: #6a6a6a;
  }
  * { box-sizing: border-box; margin: 0; padding: 0; }
  html, body {
    width: 1200px;
    height: 1000px;
    overflow: hidden;
    background: var(--page-bg);
    font-family: "Arimo", Arial, sans-serif;
  }
  .business-card {
    position: absolute;
    left: 150px;
    top: 240px;
    width: 900px;
    height: 520px;
    background: radial-gradient(ellipse 60% 70% at 50% 38%, var(--card-light) 0%, var(--card-mid) 65%, var(--card-edge) 100%);
    box-shadow: 0 10px 30px rgba(0,0,0,0.25);
    overflow: hidden;
  }
  .brand-name {
    position: absolute;
    top: 150px;
    left: 0;
    width: 100%;
    text-align: center;
    font-size: 34px;
    font-weight: 500;
    letter-spacing: 3px;
    color: var(--ink-mid);
    text-transform: uppercase;
  }
  .tagline {
    position: absolute;
    top: 322px;
    left: 0;
    width: 100%;
    text-align: center;
    font-size: 22px;
    font-weight: 500;
    letter-spacing: 1.5px;
    color: var(--ink-mid);
  }
  .service-list {
    position: absolute;
    top: 358px;
    left: 0;
    width: 100%;
    text-align: center;
    font-size: 19px;
    font-weight: 500;
    letter-spacing: 1.5px;
    color: var(--ink-dark);
  }
  .contact-band {
    position: absolute;
    left: 0;
    bottom: 0;
    width: 100%;
    height: 115px;
    background: var(--band);
    color: var(--ink-light);
    text-align: center;
  }
  .contact-numbers {
    margin-top: 24px;
    font-size: 20px;
    letter-spacing: 1.5px;
    display: flex;
    justify-content: center;
    align-items: center;
    gap: 16px;
  }
  .contact-divider {
    width: 1px;
    height: 18px;
    background: var(--divider);
  }
  .location {
    margin-top: 16px;
    font-size: 16px;
    letter-spacing: 1.5px;
    color: var(--ink-soft);
  }
</style>
</head>
<body>
  <article class="business-card">
    <h1 class="brand-name">RT Services QLD</h1>
    <p class="tagline">CARPENTRY AND BUILDING SERVICES</p>
    <p class="service-list">PROPERTY MAINTENANCE I PLASTERING I PAINTING I TILING</p>
    <footer class="contact-band">
      <p class="contact-numbers">
        <span>MARK 0412583047</span>
        <span class="contact-divider" aria-hidden="true"></span>
        <span>DEAN 0493217586</span>
      </p>
      <p class="location">BASED IN BRISBANE QLD</p>
    </footer>
  </article>
</body>
</html>
```